Floral Design for Weddings And Events

I create floral designs for weddings and events. I create unusual designs that people will remember.

Industry/Entity Type

Floral

Contact Information for Business Card

Reeds
Weddings and Events
Marlene Dukov, owner/designer
2817 Corvell Ln
Alvera Hills, CA 93164
marlyduknv@mailbrook.net
412 736-2185

Requirements
Must have
• I would like the name of the business, REEDS, to Stand Out!! I like clean, bold lines.. nothing foo-foo! Must be easy to read I'm looking for a design that catches your eye and represents my creativity. I want my card to show the potential customer that I'm unique and creative
Nice to have
• I'm thinking of the name REEDS maybe worked into the design... I'm open to your creative ideas!!!! The name must be very legible
Should not have
• I'm open to any colors other that pink and yellow..nothing Foo-Foo or flowery..

```html
<!DOCTYPE html>
<html lang="en">
<head>
<meta charset="utf-8">
<title>Reeds — Business Card</title>
<link rel="stylesheet" href="https://fonts.googleapis.com/css2?family=Arimo:wght@400&display=swap">
<style>
  :root {
    --card-bg: #212121;
    --accent: #f04e23;
    --text-light: #ffffff;
  }
  * { margin: 0; padding: 0; box-sizing: border-box; }
  html, body {
    width: 1200px;
    height: 728px;
    overflow: hidden;
    background: var(--card-bg);
  }
  .card {
    position: relative;
    width: 1200px;
    height: 728px;
    background: var(--card-bg);
    font-family: "Arimo", Arial, sans-serif;
    color: var(--text-light);
  }
  .accent-bar {
    position: absolute;
    left: 0;
    top: 0;
    width: 55px;
    height: 100%;
    background: var(--accent);
  }
  .brand {
    position: absolute;
    left: 418px;
    top: 108px;
    width: 669px;
    text-align: center;
  }
  .brand-name {
    font-size: 80px;
    font-weight: 400;
    line-height: 1;
    letter-spacing: 1px;
  }
  .brand-tagline {
    display: flex;
    align-items: center;
    gap: 12px;
    margin-top: 18px;
    color: var(--accent);
    font-size: 26px;
    line-height: 1;
  }
  .brand-tagline .rule {
    flex: 1;
    height: 2px;
    background: var(--accent);
  }
  .person {
    position: absolute;
    right: 315px;
    top: 312px;
    text-align: right;
  }
  .person-name {
    font-size: 39px;
    font-weight: 400;
    line-height: 1;
  }
  .person-role {
    margin-top: 16px;
    margin-right: 4px;
    color: var(--accent);
    font-size: 21px;
    line-height: 1;
  }
  .contact {
    position: absolute;
    right: 318px;
    top: 468px;
    text-align: right;
    font-size: 26px;
    line-height: 48px;
    list-style: none;
  }
</style>
</head>
<body>
  <main class="card">
    <div class="accent-bar"></div>

    <header class="brand">
      <h1 class="brand-name">REEDS</h1>
      <p class="brand-tagline">
        <span class="rule"></span>
        <span class="tagline-text">Weddings and Events</span>
        <span class="rule"></span>
      </p>
    </header>

    <section class="person">
      <h2 class="person-name">Marlene Dukov</h2>
      <p class="person-role">owner/designer</p>
    </section>

    <ul class="contact">
      <li class="contact-address">2817 Corvell Ln Alvera Hills, CA 93164</li>
      <li class="contact-email">marlyduknv@mailbrook.net</li>
      <li class="contact-phone">412 736-2185</li>
    </ul>
  </main>
</body>
</html>
```